Yard Sign Design for luxury design & build company

Looking to have 18" x 24" company yard signs designed.
An update to the business logo might be helpful.
Photos are not necessary but use if you can make inspiring.

Industry: Construction

Looking for a large headline of "Basement Finishing"
Website: www.tamberlyhomes.com
Phone Number (612) 555-0174
FB link: facebook.com/tamberlyhomesmn
Instagram: www.instagram.com/tamberlyhomesmn

Industry/Entity Type

Construction

Colors

Designer to choose colors to be used in the design.

Requirements
Must have
• Impactful high end characteristics
Nice to have
• Depth and detail graphis

```html
<!DOCTYPE html>
<html lang="en">
<head>
<meta charset="utf-8">
<title>Tamberly Homes – Basement Finishing Yard Sign</title>
<link rel="stylesheet" href="https://fonts.googleapis.com/css2?family=Poppins:wght@400;600;700;800&display=swap">
<style>
  :root {
    --page-bg: #ffffff;
    --sign-black: #0d0d0d;
    --photo-dark: #1c1c1c;
    --photo-mid: #2e2e2e;
    --brand-red: #d9231d;
    --text-white: #ffffff;
    --band-light: #eeeeee;
    --text-black: #111111;
    --divider: #6a6a6a;
    --badge-fill: #2a2a2a;
  }
  html, body {
    margin: 0;
    padding: 0;
    width: 773px;
    height: 1200px;
    overflow: hidden;
    background: var(--page-bg);
  }
  .canvas {
    position: relative;
    width: 773px;
    height: 1200px;
  }
  .yard-sign {
    position: absolute;
    left: 86px;
    top: 375px;
    width: 600px;
    height: 450px;
    background: var(--sign-black);
    overflow: hidden;
    box-shadow: 8px 10px 14px rgba(0,0,0,0.35);
    font-family: "Poppins", sans-serif;
  }
  .interior-photo {
    position: absolute;
    left: 0; top: 0;
    width: 600px; height: 314px;
    background: radial-gradient(ellipse at 50% 40%, var(--photo-mid) 0%, var(--photo-dark) 55%, var(--sign-black) 100%);
  }
  .brand {
    position: absolute;
    top: 20px;
    left: 0; right: 0;
    display: flex;
    justify-content: center;
    align-items: center;
    gap: 10px;
  }
  .brand-ring {
    width: 62px; height: 62px;
    border-radius: 50%;
    border: 3px solid var(--brand-red);
    box-sizing: border-box;
  }
  .brand-name {
    color: var(--text-white);
    font-weight: 600;
    font-size: 22px;
    letter-spacing: 1px;
  }
  .headline {
    position: absolute;
    left: 0; right: 0;
    text-align: center;
    margin: 0;
    font-weight: 800;
    line-height: 1;
  }
  .headline-main {
    top: 92px;
    color: var(--text-white);
    font-size: 92px;
    letter-spacing: -1px;
  }
  .headline-sub {
    top: 176px;
    color: var(--brand-red);
    font-size: 56px;
    letter-spacing: 0.33em;
    text-indent: 0.33em;
  }
  .social-handle {
    position: absolute;
    left: 40px;
    top: 254px;
    display: flex;
    align-items: center;
    gap: 10px;
    color: var(--text-white);
    font-size: 20px;
    letter-spacing: 1.5px;
  }
  .social-dot {
    width: 22px; height: 22px;
    border-radius: 50%;
    background: var(--brand-red);
  }
  .info-divider {
    position: absolute;
    left: 361px;
    top: 240px;
    width: 1px;
    height: 56px;
    background: var(--divider);
  }
  .review-badge {
    position: absolute;
    left: 393px;
    top: 238px;
    width: 164px;
    height: 58px;
    border-radius: 8px;
    background: var(--badge-fill);
  }
  .phone-band {
    position: absolute;
    left: 0; top: 314px;
    width: 600px; height: 75px;
    background: var(--brand-red);
    display: flex;
    align-items: center;
    justify-content: center;
    gap: 8px;
  }
  .phone-icon { width: 60px; height: 60px; }
  .phone-number {
    color: var(--text-white);
    font-weight: 600;
    font-size: 62px;
    letter-spacing: -2px;
    line-height: 1;
    margin-top: 6px;
  }
  .web-band {
    position: absolute;
    left: 0; top: 389px;
    width: 600px; height: 61px;
    background: var(--band-light);
    display: flex;
    align-items: center;
    justify-content: center;
  }
  .web-address {
    color: var(--text-black);
    font-weight: 700;
    font-size: 28px;
    letter-spacing: 4.5px;
  }
</style>
</head>
<body>
<div class="canvas">
  <div class="yard-sign">
    <div class="interior-photo" role="img" aria-label="Dimly lit finished basement lounge with seating and pendant lights"></div>

    <div class="brand">
      <div class="brand-ring"></div>
      <span class="brand-name">TAMBERLY HOMES</span>
    </div>

    <h1 class="headline headline-main">BASEMENT</h1>
    <h2 class="headline headline-sub">FINISHING</h2>

    <div class="social-handle">
      <span class="social-dot"></span>
      <span>@tamberlyhomesmn</span>
    </div>
    <div class="info-divider"></div>
    <div class="review-badge" role="img" aria-label="Customer review rating badge"></div>

    <div class="phone-band">
      <svg class="phone-icon" viewBox="0 0 60 60" aria-hidden="true">
        <circle cx="30" cy="30" r="30" fill="#000"/>
        <path d="M20 16c2-1 4 0 5 2l2 5c1 2 0 3-1 4l-2 2c2 4 5 7 9 9l2-2c1-1 2-2 4-1l5 2c2 1 3 3 2 5l-1 3c-1 2-3 3-6 2-11-3-19-11-22-22-1-3 0-5 3-7z" fill="#fff"/>
        <path d="M34 17a10 10 0 0 1 9 9M34 11a16 16 0 0 1 15 15" stroke="#fff" stroke-width="3" fill="none" stroke-linecap="round"/>
      </svg>
      <span class="phone-number">(612) 555-0174</span>
    </div>

    <div class="web-band">
      <span class="web-address">www.tamberlyhomes.com</span>
    </div>
  </div>
</div>
</body>
</html>
```